Insurance Agency Flyer

Create a flyer that encompasses the basic services that our agency offers. Flyer wording, logo, and company font are attached. See our website at www.tavumerix.com for additional details.

Target Market(s)

Prospective clients

Industry/Entity Type

Insurance Agency

Other font styles liked:
• baker signet com

```html
<!DOCTYPE html>
<html lang="en">
<head>
<meta charset="utf-8">
<title>The Tavumerix Company – Insurance Flyer</title>
<link rel="stylesheet" href="https://fonts.googleapis.com/css2?family=Signika:wght@300;400;600;700&display=swap">
<style>
  :root {
    --red: #e31b37;
    --red-deep: #c1202f;
    --black: #0b0b0b;
    --white: #ffffff;
    --ink: #1b1b1b;
    --grey-text: #5a5a5a;
    --backdrop: #e8ebed;
    --font: "Signika", sans-serif;
  }
  * { margin: 0; padding: 0; box-sizing: border-box; }
  html, body { width: 1200px; height: 797px; overflow: hidden; background: var(--backdrop); }
  body { font-family: var(--font); position: relative; }

  .sheet {
    position: absolute; top: 31px;
    width: 640px; height: 817px;
    transform: scale(0.9); transform-origin: top left;
    overflow: hidden; background: var(--white);
    box-shadow: 0 2px 8px rgba(0,0,0,.18);
  }
  .sheet--front { left: 16px; }
  .sheet--back { left: 608px; }
  .sheet svg.art { position: absolute; inset: 0; width: 640px; height: 817px; }
  .txt { position: absolute; color: var(--white); }

  /* brand name */
  .brand { position: absolute; text-align: center; color: var(--red); font-weight: 700; line-height: .95; }
  .brand span { display: block; }

  /* front */
  .front-brand { left: 62px; top: 170px; width: 280px; }
  .front-brand .b-small { font-size: 34px; }
  .front-brand .b-big { font-size: 50px; }
  .about-title { left: 50px; top: 594px; font-size: 16px; font-weight: 300; }
  .about-title strong { font-weight: 600; }
  .about-body { left: 50px; top: 628px; width: 224px; font-size: 10.6px; line-height: 13.5px; font-weight: 300; }
  .web-bar { position: absolute; left: 0; top: 750px; width: 307px; height: 37px; background: var(--black); }
  .web-bar p { position: absolute; left: 52px; top: 6px; font-size: 19px; color: var(--white); font-weight: 300; letter-spacing: .2px; }
  .web-bar strong { font-weight: 600; }
  .agency-intro { left: 320px; top: 418px; width: 272px; text-align: center; font-size: 16px; line-height: 20px; }
  .agency-intro .lead { font-weight: 300; }
  .agency-intro .strong { font-weight: 600; }
  .agency-body { left: 324px; top: 496px; width: 268px; text-align: center; font-size: 10.7px; line-height: 13.8px; font-weight: 300; }
  .agency-body p + p { margin-top: 13.8px; }

  /* back */
  .back-brand { left: 252px; top: 140px; width: 100px; }
  .back-brand .b-small { font-size: 12px; }
  .back-brand .b-big { font-size: 18px; }
  .offer-title { left: 30px; top: 244px; width: 280px; text-align: center; font-size: 17px; line-height: 22px; font-weight: 600; }
  .coverage-head { position: absolute; color: var(--ink); font-size: 17px; font-weight: 600; }
  .coverage-head--personal { left: 77px; top: 292px; }
  .coverage-head--business { left: 73px; top: 455px; }
  .coverage-list { position: absolute; list-style: none; color: var(--white); font-size: 13px; line-height: 16.7px; }
  .coverage-list li { padding-left: 14px; position: relative; }
  .coverage-list li::before { content: ""; position: absolute; left: 0; top: 5px; width: 8px; height: 8px; border-radius: 50%; background: var(--white); }
  .coverage-list--personal { left: 77px; top: 315px; }
  .coverage-list--business { left: 77px; top: 477px; }

  .promise-title { left: 338px; top: 250px; width: 270px; text-align: center; font-size: 15px; line-height: 19px; font-weight: 600; }
  .promise-body { left: 342px; top: 302px; width: 262px; text-align: center; font-size: 12.6px; line-height: 15.8px; }
  .testimonial { left: 357px; top: 452px; width: 236px; font-size: 10.2px; line-height: 13px; font-style: italic; font-weight: 300; }
  .client-name { left: 380px; top: 556px; width: 202px; text-align: right; font-size: 12.5px; font-weight: 600; }
  .client-role { left: 380px; top: 573px; width: 200px; text-align: right; font-size: 8px; font-style: italic; font-weight: 300; }

  .footer-brand { left: 76px; top: 712px; width: 84px; }
  .footer-brand .b-small { font-size: 10px; }
  .footer-brand .b-big { font-size: 15px; }
  .office { position: absolute; left: 240px; top: 710px; width: 144px; text-align: right; color: var(--grey-text); font-size: 12px; line-height: 18px; font-weight: 300; font-style: normal; }
  .contact-rule { position: absolute; left: 400px; top: 700px; width: 1px; height: 80px; background: var(--red); }
  .contacts { position: absolute; left: 414px; top: 710px; color: var(--grey-text); font-size: 12px; line-height: 18px; font-weight: 300; }
  .contacts .row { display: flex; }
  .contacts .label { width: 74px; }
</style>
</head>
<body>

<!-- Front side -->
<section class="sheet sheet--front">
  <svg class="art" viewBox="0 0 640 817">
    <defs>
      <linearGradient id="citySky" x1="0" y1="0" x2="0" y2="1">
        <stop offset="0" stop-color="#4a6fa3"/>
        <stop offset=".22" stop-color="#d98a4e"/>
        <stop offset=".38" stop-color="#2d3f66"/>
        <stop offset=".7" stop-color="#233a63"/>
        <stop offset="1" stop-color="#1d5d8a"/>
      </linearGradient>
      <linearGradient id="village" x1="0" y1="0" x2="1" y2="1">
        <stop offset="0" stop-color="#8a8f5a"/>
        <stop offset=".5" stop-color="#b06a35"/>
        <stop offset="1" stop-color="#7a6a5c"/>
      </linearGradient>
    </defs>
    <rect class="photo-city" x="0" y="0" width="640" height="520" fill="url(#citySky)" role="img" aria-label="Photo of a city skyline and lit bridge at dusk"/>
    <path class="photo-village" d="M0 370 L240 370 C250 420 258 470 262 520 L0 545 Z" fill="url(#village)" role="img" aria-label="Photo of a small village with autumn trees"/>
    <line x1="62" y1="0" x2="150" y2="120" stroke="#c9c9c9" stroke-width="2"/>
    <line x1="72" y1="0" x2="165" y2="118" stroke="var(--red)" stroke-width="2"/>
    <path d="M250 405 C360 370 500 340 640 305 L640 817 L302 817 C292 680 280 520 250 405 Z" fill="var(--red)"/>
    <path d="M0 545 C90 522 190 512 268 510 C284 600 294 720 302 817 L0 817 Z" fill="var(--red-deep)"/>
    <path d="M256 403 C360 368 500 338 640 308" fill="none" stroke="var(--white)" stroke-width="2" opacity=".85"/>
    <path d="M258 405 C282 520 294 680 301 817" fill="none" stroke="var(--white)" stroke-width="1.5" opacity=".6"/>
    <circle cx="202" cy="244" r="150" fill="var(--white)"/>
  </svg>

  <div class="brand front-brand">
    <span class="b-small">the</span>
    <span class="b-big">tavumerix</span>
    <span class="b-small">company</span>
  </div>

  <h2 class="txt about-title">About <strong>The Tavumerix Company</strong></h2>
  <p class="txt about-body">Established in 2008, The Tavumerix Company was created on the premise that both business and individual consumers should expect more from their insurance agency and agents. The Tavumerix Company is a full-service insurance agency that specializes in tailored insurance protection, risk management, and claims.</p>

  <div class="web-bar"><p>www.<strong>tavumerix</strong>.com</p></div>

  <h1 class="txt agency-intro">
    <span class="lead">WE ARE AN</span><br>
    <span class="strong">INDEPENDENT VELMORA<br>SELECT AGENCY</span>
  </h1>
  <div class="txt agency-body">
    <p>Being an Independent Velmora Select Agency means that we take our time to make sure that we learn about your needs, and that each policy is built to specifically meet those needs. We are committed to treating you as a person not another policy number. We will work with you to identify the insurance products and services that are right for you, your family, and/or your business.</p>
    <p>We accomplish this by using our expertise and multiple insurance carrier relationships to customize your insurance program. We will explain the different coverage and options available to you, and should the need arise, we will be there to guide you through the claim process. Our promise to you is that we will return your phone calls and emails promptly and respond to your requests in a timely manner. Also, we work diligently to stay informed about the latest insurance trends to understand how they might affect our clients.</p>
  </div>
</section>

<!-- Back side -->
<section class="sheet sheet--back">
  <svg class="art" viewBox="0 0 640 817">
    <defs>
      <linearGradient id="town" x1="0" y1="0" x2="0" y2="1">
        <stop offset="0" stop-color="#3f7fd0"/>
        <stop offset=".35" stop-color="#9fbde0"/>
        <stop offset=".55" stop-color="#d8b46a"/>
        <stop offset=".8" stop-color="#b5533e"/>
        <stop offset="1" stop-color="#5d6a70"/>
      </linearGradient>
    </defs>
    <rect class="photo-town" x="0" y="0" width="640" height="260" fill="url(#town)" role="img" aria-label="Photo of colourful old town houses beside a river"/>
    <path d="M0 232 C200 182 450 168 640 170 L640 600 C450 660 250 682 0 650 Z" fill="var(--red)"/>
    <path d="M320 182 C450 172 560 170 640 172 L640 600 C540 634 430 656 320 668 Z" fill="var(--black)"/>
    <path d="M0 236 C200 186 450 172 640 174" fill="none" stroke="var(--white)" stroke-width="2"/>
    <path d="M0 655 C250 688 450 664 640 606" fill="none" stroke="var(--red)" stroke-width="4"/>
    <path d="M0 640 C250 672 450 650 640 596" fill="none" stroke="var(--white)" stroke-width="3"/>
    <circle cx="302" cy="165" r="55" fill="var(--white)"/>
    <circle cx="117" cy="730" r="43" fill="var(--white)" stroke="var(--red)" stroke-width="3"/>
  </svg>

  <div class="brand back-brand">
    <span class="b-small">the</span>
    <span class="b-big">tavumerix</span>
    <span class="b-small">company</span>
  </div>

  <h2 class="txt offer-title">We Offer Complete Insurance<br>Services</h2>
  <h3 class="coverage-head coverage-head--personal">Personal Coverages</h3>
  <ul class="coverage-list coverage-list--personal">
    <li>Homeowners</li>
    <li>Automobile</li>
    <li>Renters / Condo</li>
    <li>Personal umbrella</li>
    <li>Valuable Property</li>
    <li>Life</li>
    <li>Disability</li>
    <li>Health</li>
  </ul>
  <h3 class="coverage-head coverage-head--business">Business Coverages</h3>
  <ul class="coverage-list coverage-list--business">
    <li>Commercial General Liability</li>
    <li>Commercial Property</li>
    <li>Workers' Compensation</li>
    <li>Business Automobile</li>
    <li>Commercial Excess Liability</li>
    <li>Professional Liability</li>
    <li>Employment Practices Liability</li>
    <li>Life</li>
    <li>Health</li>
  </ul>

  <h2 class="txt promise-title">A PROFESSIONAL AGENCY WITH<br>EXCEPTIONAL SERVICE</h2>
  <p class="txt promise-body">The Tavumerix Company is a firm of proven professionals who are dedicated to caring and conscientious service. We are committed to a high standard of excellence in all that we do and strive to establish a firm relationship of mutual trust and service with each of our clients.</p>
  <blockquote class="txt testimonial">" The Tavumerix Company has consistently responded to the needs of our business, finding us well priced policies without sacrificing coverage. They always respond to our needs quickly and effectively, provide great consultation, are knowledgeable, and care greatly about our business and success."</blockquote>
  <p class="txt client-name">Dana Whitfield</p>
  <p class="txt client-role">Long Time Client</p>

  <div class="brand footer-brand">
    <span class="b-small">the</span>
    <span class="b-big">tavumerix</span>
    <span class="b-small">company</span>
  </div>

  <address class="office">
    Main Office<br>
    2480 Harlow Avenue<br>
    Fairmont, SC 29611
  </address>
  <div class="contact-rule"></div>
  <div class="contacts">
    <div class="row"><span class="label">Phone No.</span><span>(555) 014-0800</span></div>
    <div class="row"><span class="label">Alternate No.</span><span>(555) 014-0806</span></div>
    <div class="row"><span class="label">Fax No.</span><span>(555) 014-0900</span></div>
  </div>
</section>

</body>
</html>
```